Fabric Softener

We need fabric softener. Bottle picture attached for reference. Color of bottle can be proposed as well. Normally bottle is pink and blue color

Logo is also attached that shall be used.
Updates

Need extra days to review

Low designer entries

Target Market(s)

Niche

Font styles to use
Sans Serif

Requirements
Must have
• Fabric, Brightness, Nature
Nice to have
• Good colors
Should not have
• Adults

```html
<!DOCTYPE html>
<html lang="en">
<head>
<meta charset="UTF-8">
<title>Velora Fabric Softener – Label</title>
<link rel="stylesheet" href="https://fonts.googleapis.com/css2?family=Montserrat:wght@600;700&family=Norican&display=swap">
<style>
  :root {
    --backdrop: #6ec3f0;
    --petal-light: #f08cfa;
    --petal-pale: #f6b4fb;
    --petal-mid: #c47fd4;
    --petal-deep: #8a4fa0;
    --petal-shadow: #2e1a36;
    --brand-violet: #6b5ca8;
    --title-white: #ffffff;
    --title-outline: #f218c6;
    --volume-white: #ffffff;
  }
  * { margin: 0; padding: 0; box-sizing: border-box; }
  html, body { width: 857px; height: 1200px; overflow: hidden; }
  body { background: var(--backdrop); position: relative; font-family: "Montserrat", sans-serif; }

  .label {
    position: absolute;
    left: 128px; top: 178px;
    width: 600px; height: 844px;
    border-radius: 140px 40px 70px 70px / 220px 40px 70px 70px;
    overflow: hidden;
  }
  .flower-photo {
    position: absolute; inset: 0;
    background:
      radial-gradient(ellipse 45% 28% at 62% 14%, var(--petal-pale) 0%, transparent 75%),
      radial-gradient(ellipse 50% 30% at 40% 32%, var(--petal-light) 0%, transparent 80%),
      radial-gradient(ellipse 45% 28% at 62% 58%, var(--petal-mid) 0%, transparent 80%),
      radial-gradient(ellipse 55% 25% at 50% 92%, var(--petal-shadow) 0%, transparent 85%),
      linear-gradient(180deg, var(--petal-light) 0%, var(--petal-mid) 45%, var(--petal-deep) 75%, var(--petal-shadow) 100%);
  }

  .brand {
    position: absolute;
    left: 50px; top: 240px;
    display: flex; align-items: center; gap: 16px;
  }
  .brand-mark {
    width: 44px; height: 44px;
    background: var(--brand-violet);
  }
  .brand-name {
    font-family: "Montserrat", sans-serif;
    font-weight: 700;
    font-size: 68px;
    line-height: 1;
    color: var(--brand-violet);
  }

  .product-title {
    position: absolute;
    left: 26px; top: 418px;
    font-family: "Norican", cursive;
    font-weight: 400;
    font-size: 96px;
    line-height: 1.12;
    color: var(--title-white);
    -webkit-text-stroke: 9px var(--title-outline);
    paint-order: stroke fill;
  }
  .product-title span { display: block; }
  .product-title .line-one { margin-left: 6px; }

  .volume {
    position: absolute;
    left: 150px; top: 790px;
    font-family: "Montserrat", sans-serif;
    font-weight: 600;
    font-size: 40px;
    line-height: 1;
    color: var(--volume-white);
  }
</style>
</head>
<body>
  <section class="label">
    <div class="flower-photo" role="img" aria-label="Close-up photograph of soft pink and violet flower petals fading into dark purple leaves"></div>

    <div class="brand">
      <span class="brand-mark"></span>
      <span class="brand-name">Velora</span>
    </div>

    <h1 class="product-title">
      <span class="line-one">Fabric</span>
      <span class="line-two">Softener</span>
    </h1>

    <p class="volume">1.5l</p>
  </section>
</body>
</html>
```